Stylise 5 diagrams to feature on webpage

We need existing diagrams recreated in a stylized format to go on our web page.

We will provide all required drafts and are after a style/design set which will work with our brand identity, target market and existing website.

Company Background
- We are a provider of data, software and services which blue chip companies use to shape their customer experience. ie very high tier companies, so our audience are of a high calibre.

What we want to present is clarity of thought, expertise and authority (ie we deal in data so a certain amount of conservatism is required to inspire trust in our data). However we dont want this to appear old and 'stuffy'. We want to present as the savvy partner who know their stuff but at the same time are modern and innovative and fresh.
So I am imagining crisp, clean, slick and innovative.

Potential for ongoing work
This project will have a number of images to recreate initially. However we will need an ongoing service/provider which can duplicate the style.
Other pieces may include designing PPT templates, presentations, reports, web, brochures etc

Website that the diagrams will live within.
http://new.quillmarkdata.com.au/ this is the start of the new web page. the images will sit inside the content and will need to 'balance' the currently high text to image ratio and work with the existing logo and style.
Please don't let the existing website limit your creativity or inspiration - we are open to improving our design elements :) What I do want to retain in alignment with the website is simplicity and 'crisp', ie use of clean fonts and sharp colours.

Attached are our existing brand guides. Again, please observe these loosely but feel free to offer up any improvements. The key here is that the Aubergine key colour is respected.

NOTE: Both attached files are the same but in different formats as some were having troubles opening.

Target Market(s)

Target Market(s)
- Executives of large blue chip companies (think airlines, telcos, etc).
- Consulting firms (think Hollingford Brackett, RTVW, Garrowby)

Industry/Entity Type

Software

Requirements
Must have
• Must haves
- PSD editable format for text, graphics, all elements
- the diagrams required must look to be of the same design 'family'. Once we establish this style we can progress to develop all the required diagrams and in future create a rship where we develop additional company collateral

```html
<!DOCTYPE html>
<html lang="en">
<head>
<meta charset="utf-8">
<title>Listen, Act, Discover, Improve cycle</title>
<link rel="stylesheet" href="https://fonts.googleapis.com/css2?family=Source+Sans+3:wght@400;600&display=swap">
<style>
  :root {
    --canvas-bg: #ffffff;
    --aubergine: #4f2346;
    --aubergine-deep: #3a1833;
    --aubergine-soft: #efe6ed;
  }
  html, body {
    margin: 0;
    padding: 0;
    width: 1200px;
    height: 854px;
    overflow: hidden;
    background: var(--canvas-bg);
  }
  .cycle-diagram {
    display: block;
    width: 1200px;
    height: 854px;
    background: var(--canvas-bg);
  }
  .cycle-field {
    fill: var(--aubergine-soft);
  }
  .cycle-ring {
    fill: none;
    stroke: var(--aubergine);
    stroke-width: 19;
  }
  .cycle-arrowhead {
    fill: var(--aubergine);
    stroke: var(--aubergine);
    stroke-width: 4;
    stroke-linejoin: round;
  }
  .stage-label {
    font-family: "Source Sans 3", "Myriad Pro", Arial, sans-serif;
    font-size: 47px;
    font-weight: 400;
    fill: var(--aubergine-deep);
    dominant-baseline: middle;
  }
</style>
</head>
<body>
<svg class="cycle-diagram" viewBox="0 0 1200 854" role="img" aria-label="Continuous cycle: Listen, Act, Discover, Improve">
  <circle class="cycle-field" cx="628" cy="424" r="252"/>
  <circle class="cycle-ring" cx="628" cy="424" r="262"/>

  <polygon class="cycle-arrowhead" points="576,136 666,162 576,188"/>
  <polygon class="cycle-arrowhead" points="864,368 916,368 890,456"/>
  <polygon class="cycle-arrowhead" points="688,660 598,686 688,712"/>
  <polygon class="cycle-arrowhead" points="340,462 392,462 366,374"/>

  <text class="stage-label stage-listen" x="614" y="72" text-anchor="middle">Listen</text>
  <text class="stage-label stage-act" x="964" y="400" text-anchor="start">Act</text>
  <text class="stage-label stage-discover" x="668" y="774" text-anchor="middle">Discover</text>
  <text class="stage-label stage-improve" x="300" y="404" text-anchor="end">Improve</text>
</svg>
</body>
</html>
```